I need creative and unique business card design using my company logo. Ok to change logo color. We are a small brokerage doing both Real Estate and Mortgage services. Need to have the follow on business card;
1. agent name - Mila Fenton - Realtor
2. cell - 949-555-0182
3. license number - DRE 04917362
4. business name - Brightway Estates & Lending, Inc
5. business office - 626-555-0147
6. business address - 287 W. Larkmoor Ave #214, Arcadia CA 91088
7. business logo - attached (ok to use different color on logo)

```html
<!DOCTYPE html>
<html lang="en">
<head>
<meta charset="utf-8">
<title>Brightway Estates &amp; Lending – Business Card</title>
<link rel="stylesheet" href="https://fonts.googleapis.com/css2?family=Arimo:wght@400;700&family=Montserrat:wght@500&display=swap">
<style>
  :root {
    --backdrop: #bdbdbd;
    --card-white: #ffffff;
    --brand-blue: #2f66b0;
    --brand-deep: #1f4f9c;
    --brand-light: #4a9ad6;
    --text-grey: #555555;
    --rule-grey: #8a8a8a;
  }
  * { margin: 0; padding: 0; box-sizing: border-box; }
  html, body { width: 1200px; height: 801px; overflow: hidden; }
  body {
    background: var(--backdrop);
    position: relative;
    font-family: "Arimo", Arial, sans-serif;
  }
  .card {
    position: absolute;
    top: 252px;
    width: 520px;
    height: 297px;
    border-radius: 24px;
    overflow: hidden;
    box-shadow: 0 10px 24px rgba(0,0,0,0.28);
  }
  .card--front { left: 60px; background: var(--card-white); }
  .card--back {
    left: 620px;
    background: linear-gradient(120deg, var(--brand-deep) 0%, var(--brand-blue) 35%, var(--brand-blue) 100%);
    display: flex;
    align-items: center;
    justify-content: center;
  }

  /* Brand name lockup */
  .brand {
    position: absolute;
    left: 34px;
    top: 78px;
    width: 200px;
    display: flex;
    flex-direction: column;
    align-items: center;
    font-family: "Montserrat", Arial, sans-serif;
    font-weight: 500;
    color: var(--brand-blue);
  }
  .brand__mark {
    width: 46px;
    height: 46px;
    background: var(--brand-blue);
    margin-bottom: 14px;
  }
  .brand__name { font-size: 22px; letter-spacing: 7px; text-indent: 7px; line-height: 1; }
  .brand__sub { font-size: 8.5px; letter-spacing: 2.4px; margin-top: 6px; white-space: nowrap; }

  .divider {
    position: absolute;
    left: 246px;
    top: 44px;
    width: 1px;
    height: 158px;
    background: var(--rule-grey);
  }

  .contact { position: absolute; left: 266px; top: 42px; color: var(--text-grey); }
  .contact__name {
    font-weight: 700;
    font-size: 22px;
    color: var(--brand-blue);
    text-transform: uppercase;
    letter-spacing: 0.3px;
    line-height: 1;
  }
  .contact__role { font-size: 14px; margin-top: 3px; }
  .contact__list { list-style: none; margin-top: 18px; font-size: 13.5px; line-height: 1.55; }
  .contact__list li { display: flex; align-items: center; gap: 8px; }
  .contact__list svg { width: 13px; height: 13px; flex: none; }
  .contact__address { margin-top: 12px; font-size: 13.5px; line-height: 1.45; padding-left: 21px; }

  .license-band {
    position: absolute;
    left: 0;
    top: 220px;
    width: 100%;
    height: 34px;
    background: linear-gradient(90deg, var(--brand-light) 0%, var(--brand-blue) 55%, var(--brand-deep) 100%);
    display: flex;
    align-items: center;
    padding-left: 150px;
    color: #ffffff;
    font-size: 15px;
  }
  .license-band strong { font-weight: 700; margin-right: 5px; }
  .license-band__square {
    position: absolute;
    right: 64px;
    top: 5px;
    width: 24px;
    height: 24px;
    background: var(--card-white);
  }
  .edge-strip {
    position: absolute;
    left: 0;
    bottom: 0;
    width: 100%;
    height: 34px;
    background: linear-gradient(90deg, var(--brand-light), #3f86cc);
  }

  .back-brand {
    display: flex;
    flex-direction: column;
    align-items: center;
    font-family: "Montserrat", Arial, sans-serif;
    font-weight: 500;
    color: #ffffff;
  }
  .back-brand__name { font-size: 40px; letter-spacing: 14px; text-indent: 14px; line-height: 1; }
  .back-brand__sub { font-size: 15px; letter-spacing: 4.6px; margin-top: 10px; white-space: nowrap; }
</style>
</head>
<body>
  <section class="card card--front" aria-label="Business card front">
    <div class="brand">
      <span class="brand__mark" aria-hidden="true"></span>
      <span class="brand__name">BRIGHTWAY</span>
      <span class="brand__sub">ESTATES &amp; LENDING, INC</span>
    </div>

    <div class="divider"></div>

    <div class="contact">
      <p class="contact__name">Mila Fenton</p>
      <p class="contact__role">Realtor</p>
      <ul class="contact__list">
        <li>
          <svg viewBox="0 0 16 16" aria-hidden="true"><path fill="#2f66b0" d="M3.6 1.5l2.3 2.6-1.3 1.7c.9 1.9 2.4 3.4 4.3 4.3l1.7-1.3 2.6 2.3-1.3 2.4C7.4 13.3 2.7 8.6 1.2 3z"/></svg>
          949-555-0182
        </li>
        <li>
          <svg viewBox="0 0 16 16" aria-hidden="true"><rect x="1.5" y="3.5" width="13" height="9" fill="none" stroke="#2f66b0" stroke-width="1.4"/><path d="M1.5 3.5L8 9l6.5-5.5" fill="none" stroke="#2f66b0" stroke-width="1.4"/></svg>
          626-555-0147
        </li>
      </ul>
      <p class="contact__address">287 W. Larkmoor Ave<br>#214, Arcadia CA 91088</p>
    </div>

    <div class="license-band">
      <strong>Lic No:</strong> DRE 04917362
      <span class="license-band__square" aria-hidden="true"></span>
    </div>
    <div class="edge-strip"></div>
  </section>

  <section class="card card--back" aria-label="Business card back">
    <div class="back-brand">
      <span class="back-brand__name">BRIGHTWAY</span>
      <span class="back-brand__sub">ESTATES &amp; LENDING, INC</span>
    </div>
  </section>
</body>
</html>
```